External Window Signage Design - Dentist

We have 5 windows that need to have new signage designed for a Dental Clinic based in a community shopping centre.
The windows mostly line up but there is one smaller window which is lower to the ground. All 5 windows are to be covered with vinyl graphics
The windows all face the shopping centre car park under an awning.

We have attached the measurements of the window to have graphics.
We will be placing perforated once way vision vinyl as a material on the external glass. We have also attach our logo design.

We would like something simple and creative for our design. Stock images should only be used to aid in aethetics but not form the basis of the design. We prefer simple custom graphics that identifies us as a clean, modern dental clinic. We are marketing ourselves as a modern fully digital clinic where all examinations are done on a big screen which photography and 3d scanners.

Please include the words below.

Marlow Ridge Dental

Children's Dentistry
Digital Dentistry
Cosmetic Dentistry
Clearvanta
Family Dental Care
Where quality meets value - This one is our slogan, and not a service. Please use it as such.
Same Day Emergency Bookings

Please include in small text our website and phone number.
www.marlowridgedental.com.au
Phone Number TBD: 87650432

Open to different colors but our main theme is blues and greens. Similar to our logo.

Target Market(s)

20 - 40 year old dental patients. Middle Class. Some retirees as well.

Industry/Entity Type

Dental Clinic

Font styles to use
Other font styles liked:
• Comfortaa

Colors
33b8a4
34a6d7

Requirements
Must have
• Simple elegant graphics. Stock photos to aid in design if needed.
Nice to have
• Simple designs with greys, greens and blues. As per our logo.
Comfortaa font
Should not have
• Overbearing stock imagery.
Too many colors.

```html
<!DOCTYPE html>
<html lang="en">
<head>
<meta charset="utf-8">
<title>Marlow Ridge Dental – Window Signage</title>
<link rel="stylesheet" href="https://fonts.googleapis.com/css2?family=Poppins:wght@400;500&display=swap">
<style>
  :root {
    --bg: #4a4a4c;
    --blue: #1193dc;
    --blue-light: #7cc4ef;
    --green: #6cbf45;
    --green-light: #a6dc86;
    --teal: #33b8a4;
    --white: #ffffff;
    --ink: #2f3338;
    --photo-skin: #e9dcd3;
    --photo-cool: #cfe3ef;
  }
  html, body { margin: 0; padding: 0; overflow: hidden; }
  body {
    width: 1149px; height: 1200px;
    background: var(--bg);
    font-family: "Poppins", sans-serif;
    position: relative;
  }
  .window-set { position: absolute; left: 27px; top: 379px; width: 1094px; height: 442px; }
  .pane { position: absolute; top: 0; height: 442px; overflow: hidden; background: var(--blue); }
  .pane svg.art { position: absolute; inset: 0; }
  .pane--side-left  { left: 0;   width: 121px; }
  .pane--patient    { left: 143px; width: 237px; }
  .pane--services   { left: 390px; width: 237px; }
  .pane--child      { left: 637px; width: 236px; }
  .pane--side-right { left: 890px; width: 204px; }

  .brand {
    position: absolute; left: 0; right: 0;
    display: flex; align-items: center; justify-content: center; gap: 5px;
    color: var(--blue); font-weight: 400; letter-spacing: .02em; white-space: nowrap;
  }
  .brand__dot { border-radius: 50%; background: var(--green); flex: none; }
  .brand--stacked { flex-direction: column; text-align: center; line-height: 1.2; gap: 6px; }
  .brand--light { color: var(--white); }
  .brand--light .brand__dot { background: var(--white); }

  .contact {
    position: absolute; left: 0; right: 0; text-align: center;
    color: var(--white); font-size: 7px; line-height: 1;
  }
  .contact__phone { display: flex; align-items: center; justify-content: center; gap: 5px; }

  .services { position: absolute; left: 28px; top: 232px; right: 10px; }
  .services__title { margin: 0 0 6px; color: var(--blue); font-size: 11.5px; font-weight: 500; }
  .services__list { list-style: none; margin: 0; padding: 0 0 0 16px; }
  .services__list li {
    position: relative; color: var(--ink); font-size: 10.5px; line-height: 25px;
  }
  .services__list li::before {
    content: ""; position: absolute; left: -13px; top: 11px;
    width: 4px; height: 4px; background: var(--teal); transform: rotate(45deg);
  }
  .services__list li.slogan { font-weight: 500; }
</style>
</head>
<body>
<main class="window-set">

  <!-- narrow left window -->
  <section class="pane pane--side-left">
    <svg class="art" width="121" height="442" viewBox="0 0 121 442">
      <polygon points="0,0 121,0 121,195 60,226 0,195" fill="var(--white)"/>
      <polyline points="0,197 60,228 121,197" fill="none" stroke="var(--green)" stroke-width="4"/>
      <g stroke-width="3">
        <line x1="0" y1="32" x2="30" y2="0" stroke="var(--green-light)"/>
        <line x1="10" y1="48" x2="54" y2="0" stroke="var(--blue-light)"/>
        <line x1="88" y1="28" x2="114" y2="0" stroke="var(--green-light)"/>
        <line x1="96" y1="36" x2="121" y2="10" stroke="var(--blue-light)"/>
        <line x1="0" y1="340" x2="121" y2="235" stroke="var(--blue-light)" opacity=".55"/>
        <line x1="40" y1="442" x2="121" y2="372" stroke="var(--green-light)"/>
        <line x1="60" y1="442" x2="121" y2="390" stroke="var(--blue-light)"/>
      </g>
    </svg>
    <div class="brand brand--stacked" style="top:92px;font-size:11px;">
      <span class="brand__dot" style="width:18px;height:18px;"></span>
      <span>Marlow Ridge<br>Dental</span>
    </div>
  </section>

  <!-- patient photo window -->
  <section class="pane pane--patient">
    <svg class="art" width="237" height="442" viewBox="0 0 237 442">
      <defs>
        <linearGradient id="patientTone" x1="0" y1="0" x2="1" y2="1">
          <stop offset="0" stop-color="#f4f1ee"/>
          <stop offset=".6" stop-color="var(--photo-skin)"/>
          <stop offset="1" stop-color="var(--photo-cool)"/>
        </linearGradient>
      </defs>
      <rect x="0" y="0" width="237" height="150" fill="var(--white)"/>
      <line x1="0" y1="148" x2="237" y2="148" stroke="var(--green)" stroke-width="4"/>
      <polygon points="118,85 227,146 227,270 118,332 10,270 10,146" fill="var(--white)" stroke="var(--green)" stroke-width="5"/>
      <polygon points="118,97 216,152 216,264 118,320 21,264 21,152" fill="url(#patientTone)" role="img" aria-label="Photo of a smiling young woman during a dental check-up"/>
      <g stroke-width="3">
        <line x1="110" y1="442" x2="237" y2="330" stroke="var(--green-light)"/>
        <line x1="150" y1="442" x2="237" y2="365" stroke="var(--blue-light)"/>
        <line x1="0" y1="430" x2="40" y2="395" stroke="var(--blue-light)" opacity=".6"/>
      </g>
    </svg>
    <div class="brand" style="top:44px;font-size:13px;">
      <span class="brand__dot" style="width:15px;height:15px;"></span>
      <span>Marlow Ridge Dental</span>
    </div>
    <div class="contact" style="top:345px;">www.marlowridgedental.com.au</div>
    <div class="contact contact__phone" style="top:367px;">
      <svg width="9" height="8" viewBox="0 0 24 22"><path fill="var(--white)" d="M2 6c0-3 4-5 10-5s10 2 10 5v2h-6V5H8v3H2zM6 10h12l3 10H3z"/></svg>
      <span>TBD : 87650432</span>
    </div>
  </section>

  <!-- centre services window -->
  <section class="pane pane--services">
    <svg class="art" width="237" height="442" viewBox="0 0 237 442">
      <polygon points="0,240 118,172 237,240 237,442 0,442" fill="var(--white)"/>
      <polyline points="0,237 118,168 237,237" fill="none" stroke="var(--green)" stroke-width="5"/>
      <g stroke-width="3">
        <line x1="180" y1="38" x2="222" y2="0" stroke="var(--green-light)"/>
        <line x1="196" y1="42" x2="237" y2="6" stroke="var(--blue-light)"/>
        <line x1="0" y1="30" x2="30" y2="3" stroke="var(--blue-light)" opacity=".6"/>
      </g>
    </svg>
    <div class="brand brand--stacked brand--light" style="top:50px;font-size:18px;">
      <span class="brand__dot" style="width:30px;height:30px;"></span>
      <span>Marlow Ridge Dental</span>
    </div>
    <div class="services">
      <h2 class="services__title">MARLOW RIDGE DENTAL</h2>
      <ul class="services__list">
        <li>Children's Dentistry</li>
        <li>Digital Dentistry</li>
        <li>Cosmetic Dentistry</li>
        <li>Clearvanta</li>
        <li>Family Dental Care</li>
        <li class="slogan">Where quality meets value</li>
        <li>Same Day Emergency Bookings</li>
      </ul>
    </div>
  </section>

  <!-- child photo window -->
  <section class="pane pane--child">
    <svg class="art" width="236" height="442" viewBox="0 0 236 442">
      <defs>
        <linearGradient id="childTone" x1="0" y1="0" x2="1" y2="1">
          <stop offset="0" stop-color="#d9c4ad"/>
          <stop offset=".55" stop-color="var(--photo-skin)"/>
          <stop offset="1" stop-color="#b9bde6"/>
        </linearGradient>
      </defs>
      <rect x="0" y="0" width="236" height="140" fill="var(--white)"/>
      <line x1="0" y1="138" x2="236" y2="138" stroke="var(--green)" stroke-width="4"/>
      <polygon points="118,95 226,155 226,272 118,325 10,272 10,155" fill="var(--white)" stroke="var(--green)" stroke-width="5"/>
      <polygon points="118,106 216,161 216,266 118,314 20,266 20,161" fill="url(#childTone)" role="img" aria-label="Photo of a young boy having his teeth checked"/>
      <g stroke-width="3">
        <line x1="120" y1="442" x2="236" y2="340" stroke="var(--green-light)"/>
        <line x1="0" y1="420" x2="60" y2="365" stroke="var(--blue-light)" opacity=".6"/>
      </g>
    </svg>
    <div class="brand" style="top:63px;font-size:13px;">
      <span class="brand__dot" style="width:15px;height:15px;"></span>
      <span>Marlow Ridge Dental</span>
    </div>
  </section>

  <!-- lower right window -->
  <section class="pane pane--side-right">
    <svg class="art" width="204" height="442" viewBox="0 0 204 442">
      <polygon points="0,0 204,0 204,215 102,273 0,215" fill="var(--white)"/>
      <polyline points="0,217 102,276 204,217" fill="none" stroke="var(--green)" stroke-width="5"/>
      <g stroke-width="3">
        <line x1="0" y1="46" x2="44" y2="0" stroke="var(--green-light)"/>
        <line x1="12" y1="58" x2="70" y2="0" stroke="var(--blue-light)"/>
        <line x1="156" y1="40" x2="196" y2="0" stroke="var(--green-light)"/>
        <line x1="168" y1="48" x2="204" y2="12" stroke="var(--blue-light)"/>
        <line x1="40" y1="442" x2="204" y2="300" stroke="var(--green-light)"/>
        <line x1="70" y1="442" x2="204" y2="326" stroke="var(--blue-light)"/>
      </g>
    </svg>
    <div class="brand brand--stacked" style="top:112px;font-size:16px;">
      <span class="brand__dot" style="width:30px;height:30px;"></span>
      <span>Marlow Ridge<br>Dental</span>
    </div>
  </section>

</main>
</body>
</html>
```